BENEATH THE [HARBOR] OF A DAWN, Mend your road

We are looking for a cover refresh of an existing bestselling book that is going into 3rd edition print this year.
The book is an inspirational as well as educational book that has become recognized as one of the most comprehensive, actionable, personal and financial planning resources available today for families, individuals and business owners alike.
Comprised of three true stories of loss, learning to live and love again and a 30 page checklist at the back of the book it contains tips and strategies for everyone to help them to get their personal and financial lives in order while they can.
The cover must have the following:
1. Appeal to a broad audience/both personal and corporate
2. Include Mara Quellton Bestselling Author
3. Include introduction of a new Afterword
4. 3rd Edition
5. Colors to remain the same – red, black and white
6. The title must remain in caps and the word [HARBOR] must have the brackets around it
We have also added a current copy of the second edition to help you. For your information our website is www.thequelltonhouse.example
Reason: We have narrowed it down to our top 3 designs. We are submitting the covers to our community for them to pick the top cover. Good luck to everyone

```html
<!DOCTYPE html>
<html lang="en">
<head>
<meta charset="utf-8">
<title>Beneath the [Harbor] of a Dawn — Cover</title>
<link rel="stylesheet" href="https://fonts.googleapis.com/css2?family=Crimson+Text:wght@400;600&family=Dancing+Script:wght@500&display=swap">
<style>
  :root {
    --backdrop: #e9e9e9;
    --paper: #ffffff;
    --ink: #111111;
    --red: #b8000b;
    --disc: #e6e6e6;
    --pattern: #f4f4f4;
    --photo-light: #f7f7f7;
    --photo-mid: #d9d9d9;
  }
  * { box-sizing: border-box; margin: 0; padding: 0; }
  html, body { width: 1200px; height: 800px; overflow: hidden; }
  body {
    background: var(--backdrop);
    display: flex; align-items: center; justify-content: center;
    font-family: "Crimson Text", Georgia, serif;
    color: var(--ink);
  }
  .cover {
    position: relative;
    width: 480px; height: 720px;
    background: var(--paper);
    overflow: hidden;
  }
  .cover__pattern {
    position: absolute; left: 0; top: 0; width: 100%; height: 300px;
    background: linear-gradient(180deg, var(--pattern), var(--paper));
  }
  .cover__frame {
    position: absolute; inset: 0; width: 100%; height: 100%;
    pointer-events: none;
  }
  .title-disc {
    position: absolute; left: 130px; top: 44px;
    width: 200px; height: 200px; border-radius: 50%;
    background: var(--disc);
  }
  .title {
    position: absolute; left: 0; right: 0; top: 66px;
    text-align: center; font-weight: 400; line-height: 1;
    text-transform: uppercase;
  }
  .title__line { display: block; font-size: 40px; letter-spacing: 1px; }
  .title__key { display: block; font-size: 60px; margin: 10px 0 8px; color: var(--red); letter-spacing: 1px; }
  .title__key .dark { color: var(--ink); }
  .band {
    position: absolute; left: 0; width: 100%;
    background: var(--red); color: var(--paper); text-align: center;
  }
  .band--edition-top { top: 300px; height: 20px; }
  .afterword {
    position: absolute; left: 0; width: 100%; top: 320px; height: 36px;
    background: var(--paper);
    font-family: "Dancing Script", cursive; font-size: 24px;
    text-align: center; line-height: 36px;
  }
  .band--edition { top: 356px; height: 58px; font-family: "Dancing Script", cursive; font-size: 28px; line-height: 58px; }
  .band--edition sup { font-size: 16px; }
  .cover__photo {
    position: absolute; left: 0; top: 414px; width: 100%; height: 204px;
    background: radial-gradient(ellipse at 45% 55%, var(--photo-mid), var(--photo-light) 70%);
  }
  .band--author { top: 618px; height: 72px; padding-top: 10px; }
  .author__label { display: block; font-size: 12px; letter-spacing: 1px; font-weight: 600; }
  .author__name { display: block; font-size: 28px; letter-spacing: 2px; line-height: 1.2; }
</style>
</head>
<body>
  <main class="cover">
    <div class="cover__pattern" role="img" aria-label="Faint pattern of grey feathers"></div>
    <div class="title-disc"></div>
    <h1 class="title">
      <span class="title__line">Beneath the</span>
      <span class="title__key">[HARB<span class="dark">O</span>R]</span>
      <span class="title__line">Of a Dawn</span>
    </h1>
    <div class="band band--edition-top"></div>
    <p class="afterword">Introduction of a new Afterword</p>
    <p class="band band--edition">3<sup>rd</sup> edition</p>
    <div class="cover__photo" role="img" aria-label="Photograph of an open black and silver fountain pen with its cap on white paper"></div>
    <p class="band band--author">
      <span class="author__label">BESTSELLING AUTHOR</span>
      <span class="author__name">MARA QUELLTON</span>
    </p>
    <svg class="cover__frame" viewBox="0 0 480 720" aria-hidden="true">
      <path d="M14 16 L466 13 L468 704 L12 707 Z" fill="none" stroke="#111" stroke-width="1.5"/>
      <path d="M18 12 L470 18 L463 708 L16 702 Z" fill="none" stroke="#111" stroke-width="0.8"/>
    </svg>
  </main>
</body>
</html>
```